Business card for Financial Technology company

Hello! We'd like to create business cards for 4 members of our company. Our company is a financial technology business that provides funding for businesses. We want to give it a VC (venture captal) look and feel. Clean, fresh and minimal but with a flair of artistry. I'll include some samples of cards we like. It would be great if the back of the card was artistic (see sample files 1 and 2) and the front of the card was the business info. The name of the company is Q8 Funding.

```html
<!DOCTYPE html>
<html lang="en">
<head>
<meta charset="utf-8">
<title>Northvale Funding – Business Card</title>
<link rel="stylesheet" href="https://fonts.googleapis.com/css2?family=Signika:wght@300;400;600&display=swap">
<style>
  :root {
    --backdrop: #3b3b3d;
    --card: #ffffff;
    --sky: #29a9e0;
    --navy: #1b5b8a;
    --ink: #1e1e1e;
    --magenta: #d4147f;
    --green: #4aa631;
    --orange: #f58634;
    --red: #ee3a43;
  }
  * { box-sizing: border-box; margin: 0; padding: 0; }
  html, body { width: 1200px; height: 1059px; overflow: hidden; }
  body {
    background: var(--backdrop);
    font-family: "Signika", sans-serif;
    font-weight: 300;
    color: var(--ink);
    position: relative;
  }
  .card {
    position: absolute;
    background: var(--card);
    border-radius: 24px;
    overflow: hidden;
  }
  .card--front { left: 256px; top: 100px; width: 688px; height: 391px; }
  .card--back  { left: 253px; top: 537px; width: 694px; height: 394px; }

  .corner-pattern {
    position: absolute; left: 0; top: 0; width: 240px; height: 200px;
    background: linear-gradient(135deg, rgba(180,200,235,.35), rgba(200,235,215,.3) 45%, rgba(250,210,215,.25) 70%, rgba(255,255,255,0) 90%);
    clip-path: polygon(0 0, 100% 0, 45% 100%, 0 85%);
  }

  .brand {
    position: absolute; right: 26px; top: 112px;
    display: flex; align-items: center; gap: 10px;
    font-weight: 600; font-size: 28px; line-height: 34px; color: var(--navy);
  }
  .brand__square { width: 20px; height: 20px; background: var(--magenta); }

  .name-tab {
    position: absolute; left: 0; top: 217px; width: 15px; height: 41px;
    background: var(--magenta); border-radius: 0 5px 5px 0;
  }
  .person__name {
    position: absolute; left: 26px; top: 210px;
    font-size: 34px; font-weight: 600; line-height: 36px; letter-spacing: .3px;
    white-space: nowrap;
  }
  .person__first { color: var(--sky); }
  .person__last { color: var(--navy); }
  .person__role {
    position: absolute; left: 26px; top: 243px;
    font-size: 17.5px; font-weight: 300; line-height: 20px;
  }

  .divider {
    position: absolute; left: 26px; right: 26px; top: 279px;
    height: 1px; background: var(--green);
  }

  .contacts { position: absolute; left: 26px; top: 298px; list-style: none; }
  .contacts li {
    display: flex; align-items: center; gap: 6px;
    font-size: 18px; line-height: 22.5px; height: 22.5px; white-space: nowrap;
  }
  .contacts svg { width: 12px; height: 12px; flex: none; }
  .contacts .accent { color: var(--red); }

  .address {
    position: absolute; right: 26px; top: 322px;
    text-align: right; font-size: 18px; line-height: 20.5px; white-space: nowrap;
  }
  .footer-bar {
    position: absolute; left: 440px; width: 222px; bottom: 0; height: 7px;
    background: var(--magenta);
  }

  .back-art {
    position: absolute; inset: 0;
    background:
      linear-gradient(120deg, rgba(74,166,49,.7), rgba(41,169,224,.65) 30%, rgba(108,54,140,.7) 55%, rgba(212,20,127,.7) 78%, rgba(250,190,30,.7));
  }
</style>
</head>
<body>
  <section class="card card--front">
    <div class="corner-pattern" role="img" aria-label="Faint multicoloured triangle pattern"></div>

    <div class="brand">
      <span class="brand__square"></span>
      <span>Northvale Funding</span>
    </div>

    <div class="name-tab"></div>
    <h1 class="person__name"><span class="person__first">DANA</span> <span class="person__last">WHITFIELD</span></h1>
    <p class="person__role">Genaral Manager</p>

    <div class="divider"></div>

    <ul class="contacts">
      <li>
        <svg viewBox="0 0 12 12"><path d="M2.5 1l2 2.2-1 1.2c.7 1.5 1.9 2.7 3.3 3.4l1.2-1 2.2 2-1 1.6C5.5 10.2 1.8 6.5 1 2z" fill="none" stroke="var(--orange)" stroke-width="1.2"/></svg>
        +014 5520 8631
      </li>
      <li>
        <svg viewBox="0 0 12 12"><rect x=".5" y="2" width="11" height="8" fill="var(--magenta)"/><path d="M.5 2l5.5 4.5L11.5 2M.5 10l4-4M11.5 10l-4-4" stroke="#fff" stroke-width=".9" fill="none"/></svg>
        hello@northvalefunding.com
      </li>
      <li>
        <svg viewBox="0 0 12 12"><circle cx="6" cy="6" r="5.5" fill="var(--green)"/><path d="M3 3.5c1 .3 1.5 1.2 1 2.2l1.2 1.3-.4 2M7.5 1.5c-.3 1 .4 1.7 1.5 1.6M8 6.5l1.6.4" stroke="#fff" stroke-width=".9" fill="none"/></svg>
        <span>www.<span class="accent">northvalefunding</span>.com</span>
      </li>
    </ul>

    <p class="address">418 Harbor Lane,<br>Westbrook 12, CA - 40217</p>

    <div class="footer-bar"></div>
  </section>

  <section class="card card--back">
    <div class="back-art" role="img" aria-label="Repeating colourful geometric pattern covering the card back"></div>
  </section>
</body>
</html>
```